Halcyon 88/3 (plot no. 9 sector 67 Noida)

We need a brochure designed for our upcoming premium office complex located in Delhi NCR. The brochure is meant to be circulated to potential tenants and property consultants.The brochure should showcase key aspects of the office complex, showcasing it as a premium "Grade A" building which has multiple energy conservation concepts. Since the building has been awarded a "ZELQ Platinum Pre-certification", this should be highlighted. The brochure should include location details, key project specifications, and renderings of the project facade. The brochure should also showcase the strength of the project developer, by giving some history of the developer's past projects. All relevant details to be included in the brochure are attached.

Target Market(s)

Potential customers and real estate brokers for leasing the office space

Industry/Entity Type

Real Estate

Font styles to use
Sans Serif

Colors

Designer to choose colors to be used in the design.

Requirements
Must have
• Cover page, location map, design detailing and brief description as per the attached documents
• Being a platinum rated Green Building, green aspects should be highlighted
Nice to have
• Bright colors and textured background
Should not have
• black must be avoided

```html
<!DOCTYPE html>
<html lang="en">
<head>
<meta charset="utf-8">
<title>Halcyon 88/3 – Project Specifications</title>
<link href="https://fonts.googleapis.com/css2?family=Nunito+Sans:wght@400;700&display=swap" rel="stylesheet">
<style>
  :root {
    --backdrop: #d9dadc;
    --blue-deep: #2a8fd0;
    --blue-mid: #5aaee0;
    --blue-light: #9fd3f2;
    --cell-fill: rgba(236, 246, 253, 0.78);
    --rule: #7dbde6;
    --ink: #2b3a4a;
  }
  * { box-sizing: border-box; margin: 0; padding: 0; }
  html, body {
    width: 1200px; height: 1200px; overflow: hidden;
    background: var(--backdrop);
    font-family: "Nunito Sans", sans-serif;
    color: var(--ink);
  }
  .page {
    position: absolute; left: 195px; top: 25px;
    width: 810px; height: 1150px;
    background: linear-gradient(160deg, var(--blue-light) 0%, var(--blue-mid) 45%, var(--blue-deep) 100%);
    overflow: hidden;
  }
  .page-waves { position: absolute; inset: 0; width: 100%; height: 100%; }
  .spec-table {
    position: absolute; left: 53px; width: 708px;
    border: 1px solid var(--rule);
    background: var(--cell-fill);
  }
  .spec-table.main { top: 47px; }
  .spec-table.highlights { top: 785px; }
  .spec-row {
    display: grid; grid-template-columns: 188px 1fr;
    border-top: 1px solid var(--rule);
  }
  .spec-row:first-child { border-top: none; }
  .spec-label {
    font-weight: 700; font-size: 14.5px;
    padding: 0 6px 0 13px;
    border-right: 1px solid var(--rule);
  }
  .spec-value { font-size: 14.5px; padding: 0 4px 0 10px; }
  .spec-label span, .spec-value span { display: block; line-height: 33.6px; }
  .spec-value.tight { font-size: 13.6px; letter-spacing: -0.2px; }
  .spec-row.first span { line-height: 40px; }
</style>
</head>
<body>
<div class="page">
  <svg class="page-waves" viewBox="0 0 810 1150" preserveAspectRatio="none" aria-hidden="true">
    <circle cx="930" cy="620" r="640" fill="#ffffff" opacity="0.22"/>
    <circle cx="520" cy="700" r="500" fill="#bfe4f8" opacity="0.35"/>
    <ellipse cx="700" cy="1120" rx="420" ry="130" fill="#c9ebfb" opacity="0.6"/>
    <circle cx="40" cy="40" r="260" fill="#ffffff" opacity="0.15"/>
  </svg>

  <div class="spec-table main">
    <div class="spec-row first"><div class="spec-label"><span>Project Size</span></div><div class="spec-value"><span>3,77,000 sq.ft</span></div></div>
    <div class="spec-row"><div class="spec-label"><span>Project Land Area</span></div><div class="spec-value"><span>2.5 Acres</span></div></div>
    <div class="spec-row"><div class="spec-label"><span>Number of Floors</span></div><div class="spec-value"><span>Basement + Stilt + 11</span></div></div>
    <div class="spec-row"><div class="spec-label"><span>Typical Floor Size</span></div><div class="spec-value"><span>1st - 10th Floor - 34,950 Sq. ft.</span><span>11th Floor - 27,500 Sq . ft.</span></div></div>
    <div class="spec-row"><div class="spec-label"><span>Sustainability</span></div><div class="spec-value"><span>ZELQ® PLATINUM Pre Certified (Energy savings to the range</span><span>of 30-40% and water saving to the range of 20-30%</span></div></div>
    <div class="spec-row"><div class="spec-label"><span>Efficiency</span></div><div class="spec-value"><span>75%</span></div></div>
    <div class="spec-row"><div class="spec-label"><span>Parking</span></div><div class="spec-value"><span>400 Cars expandable to 540</span></div></div>
    <div class="spec-row"><div class="spec-label"><span>Elevators</span></div><div class="spec-value"><span>6 Dedicated Passenger Elevators of 15 Passenger Capacity each</span><span>2 Dedicated Service elevator of Capacity 1088Kg each</span></div></div>
    <div class="spec-row"><div class="spec-label"><span>Earthquake Resistant</span><span>Structure</span></div><div class="spec-value"><span>Designed for Seismic Zone-IV</span></div></div>
    <div class="spec-row"><div class="spec-label"><span>Air Conditioning</span></div><div class="spec-value tight"><span>Central Air Conditioning with N+1 configuration of Chillers with 24*7 Service</span></div></div>
    <div class="spec-row"><div class="spec-label"><span>Power Backup</span></div><div class="spec-value"><span>100% power back-up with N+1 redundancy</span></div></div>
    <div class="spec-row"><div class="spec-label"><span>Redundancy in rising</span><span>main supply</span></div><div class="spec-value"><span>Two separate rising mains for redundancy</span></div></div>
    <div class="spec-row"><div class="spec-label"><span>Ceiling Height</span></div><div class="spec-value"><span>3.90 meters (floor to ceiling)</span></div></div>
    <div class="spec-row"><div class="spec-label"><span>Floor Loading</span></div><div class="spec-value"><span>400 Kg/ m2</span></div></div>
    <div class="spec-row"><div class="spec-label"><span>Building Management</span><span>System</span></div><div class="spec-value"><span>Building Management Systems infrastructure for the building</span><span>with integration with HVAC systems will be provided</span></div></div>
  </div>

  <div class="spec-table highlights">
    <div class="spec-row first"><div class="spec-label"><span>Location</span></div><div class="spec-value"><span>Premium Office Location on Noida-Greater Noida Expressway</span></div></div>
    <div class="spec-row"><div class="spec-label"><span>Efficient, Well</span><span>Conceived Floor</span><span>Plates</span></div><div class="spec-value"><span>&nbsp;</span><span>Centralized core</span><span>Efficient, floor plates, with 10.80*10.80M Grid size</span><span>Greater versatility in floor plan layouts</span><span>Service Balcony on each floor for placing outdoor units</span></div></div>
    <div class="spec-row"><div class="spec-label"><span>9 Feet Finished</span><span>Ceiling Heights</span></div><div class="spec-value"><span>Higher floor to ceiling heights enhances the feeling of space,</span><span>increases natural light available.</span><span>Aesthetically/visually superior interiors</span></div></div>
  </div>
</div>
</body>
</html>
```